business card design

i would like business cards designed. My business provides trade qualified personnel to the mining industry to work on heavy mobile equipment.
please put a excavator(digger) in the background in one design and have one design without so i can compare the difference.
also add info:
my logo(attached) and "mobile equipment repair and maintenance"
name: Derek Holloway
address: 57 Tarrowby RD Carmel Perth WA.
mobile: 0438120957
email: derek@ironvalemx.com

```html
<!DOCTYPE html>
<html lang="en">
<head>
<meta charset="utf-8">
<title>Ironvale Maintenance Services – Business Cards</title>
<link href="https://fonts.googleapis.com/css2?family=Montserrat:wght@600;700;800&family=Arimo:wght@400&display=swap" rel="stylesheet">
<style>
  :root {
    --page-bg: #e9ebee;
    --navy: #0b1f45;
    --brand-blue: #1e7bf0;
    --white: #ffffff;
    --ink: #0b1f45;
    --photo-sky: #e6ebee;
    --photo-machine: #d9b07a;
    --photo-ground: #ddd3c6;
    --card-shadow: 0 10px 28px rgba(11, 31, 69, 0.22);
  }
  * { box-sizing: border-box; margin: 0; padding: 0; }
  html, body {
    width: 1200px;
    height: 900px;
    overflow: hidden;
    background: var(--page-bg);
  }
  .sheet {
    position: relative;
    width: 1200px;
    height: 900px;
  }
  .card {
    position: absolute;
    left: 262px;
    width: 676px;
    height: 386px;
    overflow: hidden;
    box-shadow: var(--card-shadow);
    background: var(--white);
  }
  .card--front { top: 40px; }
  .card--back { top: 470px; }

  /* Front: photo background with company name */
  .front-photo {
    position: absolute;
    inset: 0;
    background:
      radial-gradient(ellipse 38% 45% at 34% 58%, rgba(217, 176, 122, 0.85), rgba(217, 176, 122, 0) 70%),
      radial-gradient(ellipse 30% 22% at 72% 62%, rgba(205, 170, 110, 0.7), rgba(205, 170, 110, 0) 70%),
      linear-gradient(180deg, var(--photo-sky) 0%, var(--photo-sky) 48%, var(--photo-ground) 78%, #e4ddd3 100%);
  }
  .front-brand {
    position: absolute;
    left: 0;
    right: 0;
    top: 150px;
    text-align: center;
    font-family: 'Montserrat', sans-serif;
    font-weight: 800;
    color: var(--navy);
    line-height: 1;
  }
  .front-brand .brand-name {
    display: block;
    font-size: 64px;
    letter-spacing: 2px;
  }
  .front-brand .brand-sub {
    display: block;
    margin-top: 8px;
    font-size: 13px;
    letter-spacing: 2.6px;
  }

  /* Back: details */
  .back-wave {
    position: absolute;
    inset: 0;
    width: 676px;
    height: 386px;
  }
  .holder-name {
    position: absolute;
    left: 56px;
    top: 92px;
    font-family: 'Montserrat', sans-serif;
    font-weight: 700;
    font-size: 25px;
    color: var(--ink);
    letter-spacing: 0.3px;
  }
  .back-brand {
    position: absolute;
    right: 40px;
    top: 66px;
    font-family: 'Montserrat', sans-serif;
    font-weight: 800;
    color: var(--navy);
    text-align: right;
    line-height: 1;
  }
  .back-brand .brand-name {
    display: block;
    font-size: 44px;
    letter-spacing: 1.5px;
  }
  .back-brand .brand-sub {
    display: block;
    margin-top: 6px;
    font-size: 9.5px;
    letter-spacing: 1.8px;
  }
  .contact-list {
    position: absolute;
    left: 58px;
    top: 170px;
    list-style: none;
    font-family: 'Arimo', sans-serif;
    font-size: 19px;
    color: var(--ink);
  }
  .contact-list li {
    display: flex;
    align-items: center;
    gap: 12px;
    height: 30px;
  }
  .contact-list svg {
    width: 18px;
    height: 18px;
    flex: none;
    fill: var(--navy);
  }
  .tagline {
    position: absolute;
    right: 30px;
    bottom: 40px;
    font-family: 'Arimo', sans-serif;
    font-size: 14.5px;
    color: var(--white);
    letter-spacing: 0.2px;
    text-transform: uppercase;
  }
</style>
</head>
<body>
<main class="sheet">

  <section class="card card--front">
    <div class="front-photo" role="img" aria-label="Photograph of an orange excavator and a row of heavy mining machines on a dusty yard, washed out pale"></div>
    <div class="front-brand">
      <span class="brand-name">IRONVALE</span>
      <span class="brand-sub">MAINTENANCE SERVICES PTY LTD</span>
    </div>
  </section>

  <section class="card card--back">
    <svg class="back-wave" viewBox="0 0 676 386" aria-hidden="true">
      <path d="M0,330 C200,345 360,310 480,240 C560,192 620,165 676,150 L676,386 L0,386 Z" fill="var(--navy)"/>
      <path d="M0,304 C180,322 330,300 460,238 C340,316 180,336 0,330 Z" fill="var(--brand-blue)"/>
    </svg>

    <h1 class="holder-name">DEREK HOLLOWAY</h1>

    <div class="back-brand">
      <span class="brand-name">IRONVALE</span>
      <span class="brand-sub">MAINTENANCE SERVICES PTY LTD</span>
    </div>

    <ul class="contact-list">
      <li>
        <svg viewBox="0 0 24 24"><path d="M6.6 10.8c1.4 2.8 3.8 5.1 6.6 6.6l2.2-2.2c.3-.3.7-.4 1-.2 1.1.4 2.3.6 3.6.6.6 0 1 .4 1 1V20c0 .6-.4 1-1 1C10.6 21 3 13.4 3 4c0-.6.4-1 1-1h3.5c.6 0 1 .4 1 1 0 1.3.2 2.5.6 3.6.1.3 0 .7-.2 1l-2.3 2.2z"/></svg>
        <span>0438120957</span>
      </li>
      <li>
        <svg viewBox="0 0 24 24"><path d="M2 5h20v14H2z M3.5 6.5 12 13l8.5-6.5" fill="none" stroke="var(--navy)" stroke-width="2"/></svg>
        <span>derek@ironvalemx.com</span>
      </li>
      <li>
        <svg viewBox="0 0 24 24"><path d="M12 2C8.1 2 5 5.1 5 9c0 5.2 7 13 7 13s7-7.8 7-13c0-3.9-3.1-7-7-7zm0 9.5A2.5 2.5 0 1 1 12 6.5a2.5 2.5 0 0 1 0 5z"/></svg>
        <span>57 Tarrowby RD Carmel Perth WA</span>
      </li>
    </ul>

    <p class="tagline">Mobile equipment repair and maintenance</p>
  </section>

</main>
</body>
</html>
```